Financial Service Company Need Business Card Design

This is a new startup company, first of its kind to offer this service. We facilitate the movement of deposit funds electronically between home buyers and real estate brokerages.Our customers are DOMIVANS®, real estate brokerages, and home buyers, we identify ourselves as a financial/technology company.
Not looking for anything too flashy. Just a clean design that shows the logo, contact info, etc. Company colors can be seen on attached logo, and 'coming soon page'
www.quorvanta.ca

```html
<!DOCTYPE html>
<html lang="en">
<head>
<meta charset="utf-8">
<title>Quorvanta Business Card</title>
<link href="https://fonts.googleapis.com/css2?family=Open+Sans:wght@400;600&family=Nunito+Sans:wght@800&display=swap" rel="stylesheet">
<style>
  :root {
    --bg: #e1e2e4;
    --card: #ffffff;
    --accent: #e04a2a;
    --ink: #555558;
    --text: #3c3c3e;
    --rule: #6b6b6e;
  }
  * { margin: 0; padding: 0; box-sizing: border-box; }
  html, body { width: 1200px; height: 1003px; overflow: hidden; background: var(--bg); }
  body { position: relative; font-family: "Open Sans", sans-serif; }
  .card {
    position: absolute; top: 330px; width: 560px; height: 344px;
    background: var(--card); border-radius: 16px; overflow: hidden;
    box-shadow: 10px 8px 14px rgba(0,0,0,0.28);
  }
  .card--front { left: 30px; }
  .card--back { left: 610px; }
  .brand-name {
    position: absolute; font-family: "Open Sans", sans-serif; font-weight: 600;
    color: var(--ink); letter-spacing: -0.5px; line-height: 1;
  }
  .card--front .brand-name { left: 30px; top: 36px; font-size: 36px; display: flex; align-items: center; gap: 10px; }
  .brand-square { width: 28px; height: 28px; background: var(--accent); display: inline-block; }
  .person { position: absolute; left: 30px; top: 166px; }
  .person__name { font-family: "Nunito Sans", sans-serif; font-weight: 800; font-size: 21px; color: var(--accent); line-height: 1.1; }
  .person__role { font-size: 16px; color: var(--text); line-height: 1.3; }
  .divider { position: absolute; left: 30px; top: 221px; width: 500px; height: 1px; background: var(--rule); }
  .contacts { position: absolute; left: 30px; top: 230px; list-style: none; }
  .contacts li { display: flex; align-items: center; gap: 11px; font-size: 16px; color: var(--text); height: 22px; }
  .contacts svg { width: 15px; height: 15px; fill: var(--accent); }
  .card--back .brand-name { left: 0; right: 0; top: 140px; text-align: center; font-size: 44px; }
  .back-url { position: absolute; left: 0; right: 0; top: 190px; text-align: center; font-size: 17px; color: var(--accent); }
</style>
</head>
<body>
  <section class="card card--front">
    <div class="brand-name"><span class="brand-square"></span>Quorvanta</div>
    <div class="person">
      <div class="person__name">Arlen Voss</div>
      <div class="person__role">President</div>
    </div>
    <div class="divider"></div>
    <ul class="contacts">
      <li><svg viewBox="0 0 16 16"><path d="M3 1l3 3-1.5 2c1 2 3 4 5 5L11.5 9.5l3 3-2 2.5C7 14 2 9 1 3z"/></svg>555.014.2290</li>
      <li><svg viewBox="0 0 16 16"><path d="M4 1h8a1 1 0 0 1 1 1v12a1 1 0 0 1-1 1H4a1 1 0 0 1-1-1V2a1 1 0 0 1 1-1zm1 2v9h6V3zm3 10a.8.8 0 1 0 0 .1z"/></svg>555.014.2290</li>
      <li><svg viewBox="0 0 16 16"><path d="M1 3h14v10H1zm1.5 1.2L8 8.5l5.5-4.3v-.2h-11zM2 5.5V12h12V5.5L8 10z"/></svg>info@quorvanta.ca</li>
      <li><svg viewBox="0 0 16 16"><path d="M8 1a7 7 0 1 0 0 14A7 7 0 0 0 8 1zm-1 2.2c-.5 1-1 1.5-2 1.8.5 1 1.5 1 1.8 2-.5 1-2 1-2 2.5 1 .5 1.5 2 1.5 3A5 5 0 0 1 7 3.2zm2 0a5 5 0 0 1 3.8 7.3c-1-.5-1.3-1.5-2.3-1.5-.5-1 .5-1.5 0-2.5-1 0-1.5-1-1.5-2z"/></svg>www.quorvanta.ca</li>
    </ul>
  </section>

  <section class="card card--back">
    <div class="brand-name">Quorvanta</div>
    <div class="back-url">www.quorvanta.ca</div>
  </section>
</body>
</html>
```